Creative Brief
Investment Banking Company Stationary
Business card, Letterhead, Envelope, Fax Cover
Professional
Daniyar Ospanturov
Managing Partner
27B Zheltoksan St,
Almaty, 050118
Kazakhstan
dospanturov@mailvero.kz
www.veltrafin.kz
The name of the company is Veltra Finance, LLP. In addition to the logo there should be text that includes the official name of the company.
I will need business cards for 3 other employees as well. Please message me for their relevant info.
Logo or blank

```html
<!DOCTYPE html>
<html lang="en">
<head>
<meta charset="utf-8">
<title>Veltra Finance Stationery</title>
<link rel="stylesheet" href="https://fonts.googleapis.com/css2?family=Arimo:wght@400&display=swap">
<style>
  :root {
    --backdrop: #7b7b7b;
    --paper: #ffffff;
    --earth: #75664f;
    --navy: #1f2e52;
    --ghost: #dcdee3;
    --ink: #3a3a3a;
    --light-ink: #f3efe8;
  }
  * { margin: 0; padding: 0; box-sizing: border-box; }
  html, body { width: 1200px; height: 685px; overflow: hidden; background: var(--backdrop); }
  .canvas { position: relative; width: 1200px; height: 685px; font-family: "Arimo", Arial, sans-serif; }
  .sheet { position: absolute; background: var(--paper); overflow: hidden; box-shadow: 0 1px 3px rgba(0,0,0,.25); }
  .sheet svg.shapes { position: absolute; inset: 0; }
  .brand { position: absolute; font-family: "Arimo", Arial, sans-serif; font-weight: 400; color: var(--navy); white-space: nowrap; text-transform: uppercase; letter-spacing: .04em; }
  .small { position: absolute; color: var(--ink); white-space: nowrap; line-height: 1.35; }
  .on-earth { color: var(--light-ink); text-align: right; }

  /* Letterhead */
  .letterhead { left: 180px; top: 10px; width: 504px; height: 643px; }
  .letterhead .brand { left: 22px; top: 34px; font-size: 15px; }
  .letterhead .contact-top { right: 14px; top: 22px; font-size: 7.5px; text-align: right; }
  .watermark-name { position: absolute; left: 0; width: 504px; text-align: center; top: 396px; font-family: "Arimo", Arial, sans-serif; font-weight: 400; font-size: 38px; letter-spacing: .04em; text-transform: uppercase; color: var(--ghost); white-space: nowrap; }
  .letterhead .address { right: 16px; bottom: 12px; font-size: 7.5px; }

  /* Business card */
  .card { left: 19px; top: 355px; width: 209px; height: 125px; }
  .card .brand { left: 12px; top: 22px; font-size: 6.5px; }
  .card .person { left: 118px; top: 12px; font-size: 5px; }
  .card .address { left: 12px; top: 56px; font-size: 5px; }
  .card .online { right: 12px; top: 72px; font-size: 5px; text-align: right; }

  /* Envelope */
  .envelope { position: absolute; left: 629px; top: 307px; width: 552px; height: 298px; }
  .envelope .flap { position: absolute; left: 0; top: 0; }
  .flap-brand { position: absolute; left: 0; top: 0; width: 552px; height: 84px; transform: rotate(180deg); }
  .flap-brand .brand { left: 0; width: 552px; text-align: center; top: 46px; font-size: 11px; color: var(--light-ink); }
  .envelope-body { left: 0; top: 84px; width: 552px; height: 214px; }
  .envelope-body .brand { left: 20px; top: 34px; font-size: 13px; }
  .envelope-body .address { right: 14px; bottom: 10px; font-size: 7px; }
</style>
</head>
<body>
<div class="canvas">

  <section class="sheet letterhead">
    <svg class="shapes" width="504" height="643" viewBox="0 0 504 643" aria-hidden="true">
      <path d="M0,455 C40,560 210,598 504,600 L504,643 L0,643 Z" fill="var(--earth)"/>
    </svg>
    <div class="brand">Veltra Finance</div>
    <div class="small contact-top">dospanturov@mailvero.kz<br>www.veltrafin.kz</div>
    <div class="watermark-name">Veltra Finance</div>
    <div class="small on-earth address">27B Zheltoksan St, Almaty, 050118 Kazakhstan<br>Ph: +7 (727) 315 4208 &nbsp; Fax: +7 (727) 315 4209</div>
  </section>

  <section class="sheet card">
    <svg class="shapes" width="209" height="125" viewBox="0 0 209 125" aria-hidden="true">
      <path d="M0,114 C80,112 170,104 209,92 L209,125 L0,125 Z" fill="var(--earth)"/>
    </svg>
    <div class="brand">Veltra Finance</div>
    <div class="small person">Daniyar Ospanturov<br>Managing Partner</div>
    <div class="small address">27B Zheltoksan St,<br>Almaty, 050118<br>Kazakhstan<br>T: +7 (727) 315 4208<br>M: +7 (701) 482 1163</div>
    <div class="small online">dospanturov@mailvero.kz<br>www.veltrafin.kz</div>
  </section>

  <section class="envelope">
    <svg class="flap" width="552" height="84" viewBox="0 0 552 84" aria-hidden="true">
      <path d="M8,84 L30,10 Q34,0 50,0 L502,0 Q518,0 522,10 L544,84 Z" fill="var(--earth)"/>
    </svg>
    <div class="flap-brand">
      <div class="brand">Veltra Finance</div>
    </div>
    <div class="sheet envelope-body">
      <svg class="shapes" width="552" height="214" viewBox="0 0 552 214" aria-hidden="true">
        <path d="M0,214 C150,200 400,130 552,20 L552,214 Z" fill="var(--earth)"/>
      </svg>
      <div class="brand">Veltra Finance</div>
      <div class="small on-earth address">27B Zheltoksan St, Almaty, 050118 Kazakhstan<br>Ph: +7 (727) 315 4208 &nbsp; Fax: +7 (727) 315 4209<br>Email: dospanturov@mailvero.kz &nbsp; Web: www.veltrafin.kz</div>
    </div>
  </section>

</div>
</body>
</html>
```